Financial Broker firm looking for Brochure design/Pdf-document

Job Type
Brochure Design/PDF-Document
Task Outline
Create a Brochure Design that also works for sending as pdf-document.
Task Description
We need a combined corporate brochure (Booklet style) to give out to potential clients as well as sending it to potential clients through Internet as pdf-document.
We need a background template with pictures and colors that gives the impression of professionalism, trustworthiness and seriousness. Attached text in English but the text will be translated into different languages to fit different markets. Therefore we would like to receive one template including the text and one without any text (but with the logo). Please inform us where (any) pictures and/or photos on the template have been taken from in order for us to buy and use them legally.
About Us
Our company Quelvant Partners AB is a financial brokerage company who provides a diversity of services for different selected partners (www.quelvantpartners.example).
Target Market
Companies on all levels, domestic or international
Requirements
Must Have:
-The text and logo attached below
Industry/Entity Type
Financial
Look and feel

```html
<!DOCTYPE html>
<html lang="en">
<head>
<meta charset="utf-8">
<title>Quelvant Partners AB – Brochure Spread</title>
<link rel="stylesheet" href="https://fonts.googleapis.com/css2?family=Comfortaa:wght@300;400&family=Exo+2:wght@400;500;600&display=swap">
<style>
:root{
  --stage:#e9eaec;
  --paper:#ffffff;
  --brand-blue:#1f5ea8;
  --brand-deep:#154a8a;
  --accent-light:#3d7cc4;
  --text:#2b2f36;
  --heading-soft:#4f86c6;
  --accent-orange:#e07a2a;
  --photo-sky-top:#5f88b8;
  --photo-sky-bottom:#c9d8ea;
  --photo-desk-top:#a9bfd8;
  --photo-desk-bottom:#e5edf6;
  --gutter-shadow:rgba(0,0,0,.12);
}
*{box-sizing:border-box;margin:0;padding:0}
html,body{width:1200px;height:848px;overflow:hidden;background:var(--stage)}
body{font-family:"Exo 2",Arial,sans-serif;color:var(--text)}
.spread{
  position:absolute;left:60px;top:44px;width:1080px;height:760px;
  display:flex;box-shadow:0 8px 30px rgba(0,0,0,.18);
}
.page{position:relative;width:540px;height:760px;background:var(--paper);overflow:hidden}
.page--left::after{
  content:"";position:absolute;right:0;top:0;width:40px;height:100%;
  background:linear-gradient(to left,var(--gutter-shadow),transparent);
}
.page--right::before{
  content:"";position:absolute;left:0;top:0;width:30px;height:100%;
  background:linear-gradient(to right,var(--gutter-shadow),transparent);z-index:2;
}
/* left page */
.hero-photo{
  position:absolute;left:0;top:0;width:540px;height:600px;
  background:linear-gradient(170deg,var(--brand-deep) 0%,var(--photo-sky-top) 22%,var(--photo-sky-bottom) 70%,#8ea7c4 100%);
  clip-path:polygon(0 0,100% 0,100% 100%,87% 100%,83% 73.3%,0 73.3%);
}
.hero-band{position:absolute;left:0;top:0;width:540px;height:46px;background:var(--brand-blue)}
.about{position:absolute;left:0;top:440px;width:540px;height:320px}
.about__title{
  position:absolute;left:22px;top:18px;
  font-family:"Comfortaa",Arial,sans-serif;font-weight:300;font-size:40px;
  color:var(--heading-soft);letter-spacing:.5px;white-space:nowrap;
}
.about__rule{position:absolute;left:232px;top:44px;width:1.5px;height:160px;background:var(--accent-light)}
.about__rule::before{
  content:"";position:absolute;left:-4px;top:-6px;width:9px;height:9px;border-radius:50%;
  border:1.5px solid var(--accent-light);background:var(--paper);
}
.about__text{
  position:absolute;left:246px;top:40px;width:194px;
  font-size:17px;line-height:1.38;color:var(--text);
}
.about__text strong{color:var(--brand-blue);font-weight:600}
.page-edge{position:absolute;left:0;bottom:0;width:100%;height:4px;background:var(--accent-orange)}
/* right page */
.top-wave{position:absolute;left:0;top:0;width:540px;height:120px}
.content{position:absolute;left:52px;top:112px;width:450px}
.section + .section{margin-top:18px}
.section__title{
  position:relative;padding-left:16px;
  font-size:16px;font-weight:600;color:var(--brand-blue);margin-bottom:6px;
}
.section__title::before{
  content:"";position:absolute;left:0;top:6px;width:7px;height:7px;border-radius:50%;
  border:1.5px solid var(--brand-blue);
}
.section p{font-size:11.5px;line-height:1.5;margin-bottom:9px;text-indent:16px}
.footer-photo-rule{position:absolute;left:52px;right:0;top:604px;height:3px;background:var(--brand-blue)}
.footer-photo{
  position:absolute;left:52px;right:0;top:612px;height:128px;
  background:linear-gradient(120deg,var(--photo-desk-top) 0%,var(--photo-desk-bottom) 60%,#ffffff 100%);
}
.page--right .page-edge{background:var(--brand-blue)}
</style>
</head>
<body>
<main class="spread">
  <section class="page page--left">
    <div class="hero-photo" role="img" aria-label="Photo of two business people shaking hands in front of glass skyscrapers under a blue sky"></div>
    <div class="hero-band"></div>
    <article class="about">
      <h1 class="about__title">About Us</h1>
      <span class="about__rule"></span>
      <p class="about__text"><strong>Quelvant Partners</strong> has been created to reply quickly to your liquidity, insurance and currency hedging needs. You have at your disposal a personal advisor expert in your needs.</p>
    </article>
    <div class="page-edge"></div>
  </section>

  <section class="page page--right">
    <svg class="top-wave" viewBox="0 0 540 120" preserveAspectRatio="none" aria-hidden="true">
      <path d="M0 0H540V8C420 10 330 40 250 80C190 108 120 112 0 96Z" fill="#1f5ea8"/>
    </svg>
    <div class="content">
      <section class="section">
        <h2 class="section__title">Foreign Exchange Service</h2>
        <p>If your company trades internationally, you are more than likely to make international payments. Our partners will help your company manage this process. You can save half the costs involved in the money transfer and get access to a better service compared to traditional banks.</p>
        <p>With international payments you most likely have paid or received different amounts from foreign currencies. This is called fluctuations in the currency market. The service we provide will help you to identify risks and how you can cover them. We are working with different partners that will cover your currency risks.</p>
        <p>They can also assist you with avoiding commodity risks for your production, for example protecting the price of a production commodity or interest rate risks, if you have a variable loan. The burden of a rise in the interest rate may be expensive to your company. If you are interested, there is also the option by remunerate your liquidity through our partners' cash certificate deposit.</p>
      </section>
      <section class="section">
        <h2 class="section__title">Covering Financial Risks</h2>
        <p>With international payments you most likely have paid or received different amounts from foreign currencies. This is called fluctuations in the currency market. The service we provide will help you to identify risks and how you can cover them.</p>
        <p>We are working with different partners that will cover your currency risks. They can also assist you with avoiding commodity risks for your production, for example protecting the price of a production commodity or interest rate risks, if you have a variable loan. The burden of a rise in the interest rate may be expensive to your company. If you are interested, there is also the option by remunerate your liquidity through our partners' cash certificate deposit.</p>
      </section>
    </div>
    <div class="footer-photo-rule"></div>
    <div class="footer-photo" role="img" aria-label="Close-up photo of calculator keys with a pen resting beside them"></div>
    <div class="page-edge"></div>
  </section>
</main>
</body>
</html>
```